Book Cover: Quiet Bloom: Gentle Practices For The Busy Soul

I would like a full cover spread- front, back and spine as well as a stand alone front cover for Pagewell for the book. Design a cover that mirrors the profound depth and dynamic energy of 'Quiet Bloom.' Envision a visual tapestry that draws readers into a transformative journey, where spirituality and self-care unite. Explore vibrant colors, intricate textures, and a sense of inner radiance that beckons readers to explore the book's rich wisdom within. See images for design inspiration attached. Even though some of the images are cartoon, I'd like the cover to be more serious than playful and very elegant.

About this book (back cover copy)
Are you ready to embark on a transformative journey and elevate your daily existence? "Quiet Bloom" is a treasure trove of practical yet profound rituals and wisdom from renowned self-care, healing, and spirituality experts.

Within these pages, you'll uncover a tapestry of guidance and insight from some of the world's most respected mentors. Their collective wisdom is your key to creating a sacred sanctuary within your everyday life.

From invigorating morning rituals to meditative practices, empowering affirmations, and transformative energy healing, you'll find a rich tapestry of tools to nurture a deeper connection with yourself and the universe.

Whether you're a seasoned practitioner or a newcomer to the world of self-care and spirituality, "Quiet Bloom" is your trusted companion on the journey to transform your life and elevate your daily experience. Open this book today and start your sacred, fulfilling adventure.

Colors
0094D4
00A9DD
6FCCEA
C7EBF8
E9F6FB
E54698
E96AAD
F1A4CE
F9D9EA
FCEFF6
6B429C
8869AF
B7A5CE
E3DAEB
F3F0F8

Requirements
Must have
• Title: Quiet Bloom: Subtitle: Gentle Practices For The Busy Soul Name of Publisher: Copperleaf Lantern Publishing- Logo on the back Back cover copy

```html
<!DOCTYPE html>
<html lang="en">
<head>
<meta charset="utf-8">
<title>Quiet Bloom – Cover Spread</title>
<link rel="stylesheet" href="https://fonts.googleapis.com/css2?family=Oswald:wght@700&family=Arimo:wght@400;700&display=swap">
<style>
  :root {
    --backdrop: #ecebe8;
    --paper: #ffffff;
    --paper-shade: #e6e6e8;
    --ink: #1a1a1a;
    --ink-soft: #2b2b2b;
    --plum: #6b429c;
    --plum-soft: #8869af;
    --lilac: #b7a5ce;
    --rose: #e54698;
    --rose-soft: #e96aad;
    --blush: #f1a4ce;
    --sky: #00a9dd;
    --sky-soft: #6fccea;
    --sunshine: #f6d43a;
  }
  * { box-sizing: border-box; margin: 0; padding: 0; }
  html, body {
    width: 1200px; height: 800px; overflow: hidden;
    background: var(--backdrop);
  }
  .spread {
    position: absolute; left: 150px; top: 80px;
    width: 900px; height: 640px;
    display: flex;
    box-shadow: 0 10px 30px rgba(0,0,0,0.18);
  }
  .back-cover, .spine, .front-cover {
    position: relative; height: 100%; background: var(--paper);
  }
  /* Back cover */
  .back-cover {
    width: 420px;
    padding: 86px 44px 0 50px;
  }
  .back-title {
    font-family: "Oswald", sans-serif; font-weight: 700;
    font-size: 34px; line-height: 1; text-align: center;
    letter-spacing: 0.5px;
  }
  .back-title .word-quiet { color: var(--plum); }
  .back-title .word-bloom { color: var(--rose); }
  .back-subtitle {
    font-family: "Arimo", sans-serif; font-size: 13px;
    text-transform: uppercase; text-align: center;
    color: var(--ink); line-height: 1.25; margin: 8px auto 24px;
    width: 200px;
  }
  .blurb p {
    font-family: "Arimo", sans-serif; font-size: 10.4px;
    line-height: 1.38; color: var(--ink-soft);
    margin-bottom: 13px;
  }
  .publisher-mark {
    position: absolute; left: 0; right: 0; bottom: 58px;
    text-align: center;
    font-family: "Arimo", sans-serif; font-weight: 400;
    font-size: 13px; line-height: 1.4; color: var(--ink);
  }
  /* Spine */
  .spine {
    width: 60px;
    border-left: 1px solid #f0f0f0;
    border-right: 1px solid #dcdcdf;
    background: linear-gradient(90deg, #fafafa, #ffffff 45%, #f2f2f4);
  }
  .spine-title, .spine-author {
    position: absolute; left: 50%; transform: translateX(-50%);
    writing-mode: vertical-rl;
    font-family: "Oswald", sans-serif; font-weight: 700;
  }
  .spine-title { top: 40px; font-size: 28px; letter-spacing: 0.5px; }
  .spine-title .word-quiet { color: var(--plum); }
  .spine-title .word-bloom { color: var(--rose); }
  .spine-author { bottom: 34px; font-size: 17px; color: var(--ink); }
  /* Front cover */
  .front-cover {
    width: 420px; overflow: hidden;
    background: linear-gradient(90deg, var(--paper-shade) 0%, var(--paper) 22%, var(--paper) 100%);
  }
  .front-title {
    position: absolute; right: 36px; top: 58px;
    font-family: "Oswald", sans-serif; font-weight: 700;
    text-align: right; line-height: 0.92; z-index: 2;
  }
  .front-title .word-quiet { display: block; font-size: 96px; color: var(--plum); }
  .front-title .word-bloom { display: block; font-size: 118px; color: var(--rose); }
  .portrait-art {
    position: absolute; left: 44px; top: 200px;
    width: 340px; height: 330px; z-index: 1;
  }
  .front-subtitle {
    position: absolute; left: 40px; right: 28px; top: 486px;
    font-family: "Arimo", sans-serif; font-size: 21px;
    text-transform: uppercase; text-align: center;
    color: var(--ink); line-height: 1.2; z-index: 2;
  }
  .front-author {
    position: absolute; right: 70px; bottom: 50px;
    font-family: "Oswald", sans-serif; font-weight: 700;
    font-size: 30px; color: var(--ink); z-index: 2;
  }
</style>
</head>
<body>
  <main class="spread">
    <section class="back-cover">
      <h2 class="back-title"><span class="word-quiet">QUIET</span> <span class="word-bloom">BLOOM</span></h2>
      <p class="back-subtitle">Gentle Practices For The Busy Soul</p>
      <div class="blurb">
        <p>Are you ready to embark on a transformative journey and elevate your daily existence? "Quiet Bloom" is a treasure trove of practical yet profound rituals and wisdom from renowned self-care, healing, and spirituality experts.</p>
        <p>Within these pages, you'll uncover a tapestry of guidance and insight from some of the world's most respected mentors. Their collective wisdom is your key to creating a sacred sanctuary within your everyday life.</p>
        <p>From invigorating morning rituals to meditative practices, empowering affirmations, and transformative energy healing, you'll find a rich tapestry of tools to nurture a deeper connection with yourself and the universe.</p>
        <p>Whether you're a seasoned practitioner or a newcomer to the world of self-care and spirituality, "Quiet Bloom" is your trusted companion on the journey to transform your life and elevate your daily experience. Open this book today and start your sacred, fulfilling adventure.</p>
      </div>
      <p class="publisher-mark">Copperleaf Lantern<br>Publishing</p>
    </section>

    <section class="spine">
      <span class="spine-title"><span class="word-quiet">QUIET</span> <span class="word-bloom">BLOOM</span></span>
      <span class="spine-author">AUTHOR NAME</span>
    </section>

    <section class="front-cover">
      <h1 class="front-title"><span class="word-quiet">QUIET</span><span class="word-bloom">BLOOM</span></h1>
      <svg class="portrait-art" viewBox="0 0 340 330" role="img" aria-label="Watercolour portrait of a woman in splashes of pink, purple, blue and yellow, dripping downward">
        <defs>
          <radialGradient id="wash-rose" cx="0.5" cy="0.5" r="0.5">
            <stop offset="0" stop-color="#e96aad" stop-opacity="0.75"/>
            <stop offset="1" stop-color="#e96aad" stop-opacity="0"/>
          </radialGradient>
          <radialGradient id="wash-sky" cx="0.5" cy="0.5" r="0.5">
            <stop offset="0" stop-color="#6fccea" stop-opacity="0.7"/>
            <stop offset="1" stop-color="#6fccea" stop-opacity="0"/>
          </radialGradient>
          <radialGradient id="wash-plum" cx="0.5" cy="0.5" r="0.5">
            <stop offset="0" stop-color="#8869af" stop-opacity="0.6"/>
            <stop offset="1" stop-color="#8869af" stop-opacity="0"/>
          </radialGradient>
          <radialGradient id="wash-sun" cx="0.5" cy="0.5" r="0.5">
            <stop offset="0" stop-color="#f6d43a" stop-opacity="0.7"/>
            <stop offset="1" stop-color="#f6d43a" stop-opacity="0"/>
          </radialGradient>
        </defs>
        <ellipse cx="190" cy="110" rx="130" ry="90" fill="url(#wash-rose)"/>
        <ellipse cx="120" cy="120" rx="110" ry="80" fill="url(#wash-sky)"/>
        <ellipse cx="180" cy="180" rx="110" ry="90" fill="url(#wash-plum)"/>
        <ellipse cx="230" cy="220" rx="90" ry="80" fill="url(#wash-sun)"/>
        <ellipse cx="160" cy="260" rx="120" ry="60" fill="url(#wash-rose)"/>
      </svg>
      <p class="front-subtitle">Gentle Practices For<br>The Busy Soul</p>
      <p class="front-author">AUTHOR NAME</p>
    </section>
  </main>
</body>
</html>
```